Security company needs HTML and CSS files and templates made & Blogs

need HTML files and template pages created for about us, staff, MMJ transport, vehicles, alarm systems, video systems, gaurd services, private investigations, surveillance audit request form, and compliance investigation request form, blog setup for video systems, alarm systems, and video monitoring. Needs to be Adobe Dreamweaver CS6 Format. Website needs to be based off the original PSD file. All images must be original or royalty free for use.

Target Market(s)

Customers

Industry/Entity Type

Security

Coding

Coded - Design and coding required

Number of Pages Required

5+ page

Requirements
Must have
• template pages created for about us, staff, MMJ transport, vehicles, alarm systems, video systems, gaurd services, private investigations, surveillance audit request form, and compliance investigation request form, blog setup for video systems, alarm systems, and video monitoring. Needs to be Adobe Dreamweaver CS6 Format Website needs to be based off the original PSD file
Nice to have
• Scheduling calendar built in that interfaces with Microsoft Exchange, Blogs

```html
<!DOCTYPE html>
<html lang="en">
<head>
<meta charset="utf-8">
<title>Guardline Security – Blog Posts</title>
<link href="https://fonts.googleapis.com/css2?family=Exo+2:ital,wght@1,700;1,800&family=Roboto:wght@400;500&family=Raleway:wght@400;500;600&display=swap" rel="stylesheet">
<style>
:root{
  --blue:#1f9fd8;
  --blue-dark:#1478ad;
  --footer-blue:#1676a6;
  --green:#8cc31e;
  --green-dark:#6fa314;
  --navy:#0b2345;
  --red:#d71920;
  --teal:#16a58a;
  --ink:#222;
  --body:#555;
  --rule:#d9d9d9;
  --white:#fff;
}
*{margin:0;padding:0;box-sizing:border-box}
html,body{width:1200px;height:2416px;overflow:hidden;background:var(--white)}
body{position:relative;font-family:'Raleway',sans-serif;color:var(--ink)}
.abs{position:absolute}

.topbar{left:712px;top:0;width:488px;height:38px;background:var(--blue);border-bottom-left-radius:30px;color:var(--white);font:500 16px 'Roboto',sans-serif;display:flex;align-items:center;gap:44px;padding-left:28px}
.topbar span{display:flex;align-items:center;gap:10px}
.topline{left:0;top:0;width:1200px;height:5px;background:var(--blue)}

.brand{left:100px;top:58px;display:flex;align-items:center;gap:10px;font:500 26px 'Roboto',sans-serif;color:var(--red)}
.brand i{display:block;width:22px;height:22px;border-radius:50%;background:var(--red)}
.mainnav{left:440px;top:90px;display:flex;gap:36px;font:400 16px 'Roboto',sans-serif;color:var(--ink)}

.navbar{left:0;top:152px;width:1200px;height:60px;background:linear-gradient(var(--blue),var(--blue-dark));border-bottom:3px solid var(--green)}
.navbar ul{list-style:none;display:flex;height:57px;margin-left:100px;font:400 16px 'Roboto',sans-serif;color:var(--white)}
.navbar li{display:flex;align-items:center;padding:0 18px}
.navbar li.active{background:var(--green);padding:0 26px}

.hero{left:0;top:212px;width:1200px;height:221px;background:linear-gradient(100deg,#0a1f3c 0%,#0f3563 55%,#123e6e 100%)}
.hero h1{position:absolute;left:100px;top:78px;font:italic 800 44px 'Exo 2',sans-serif;color:var(--white);text-shadow:0 2px 4px rgba(0,0,0,.4)}

.blog-title{left:0;top:462px;width:1200px;text-align:center;font:italic 800 29px 'Exo 2',sans-serif;color:var(--navy)}
.blog-title em{color:var(--red);font-style:inherit}
.blog-sub{left:0;top:512px;width:1200px;display:flex;justify-content:center;align-items:center;gap:12px;font:500 14px 'Raleway',sans-serif;color:var(--ink)}
.blog-sub b{display:block;width:62px;height:2px;background:var(--red)}

.post{left:98px;width:1004px;height:310px}
.post .photo{position:absolute;left:0;top:0;width:400px;height:300px;border:5px solid #f1f1f1;box-shadow:0 1px 5px rgba(0,0,0,.35)}
.post h2{position:absolute;left:429px;top:14px;font:500 21px 'Roboto',sans-serif;color:var(--ink)}
.meta{position:absolute;left:429px;top:55px;display:flex;gap:22px;font:500 15px 'Roboto',sans-serif;color:var(--teal)}
.meta span{display:flex;align-items:center;gap:7px}
.post p{position:absolute;left:429px;width:575px;font:400 11.6px/21px 'Raleway',sans-serif;color:var(--body)}
.post .p1{top:86px}
.post .p2{top:172px}
.readmore{position:absolute;left:431px;top:252px;width:109px;height:40px;border:2px solid #333;border-radius:5px;font:400 15px 'Roboto',sans-serif;color:var(--ink);display:flex;align-items:center;justify-content:center}
.divider{left:98px;width:1004px;height:1px;background:var(--rule)}

.footer{left:0;top:2040px;width:1200px;height:306px;background:var(--footer-blue);color:var(--white)}
.badge{left:106px;top:2090px;width:138px;height:138px;border-radius:50%;background:radial-gradient(circle,#2a3f86 0 42%,#d2b12a 43% 62%,#22366f 63%)}
.social{left:100px;top:2252px;display:flex;gap:8px}
.social i{display:block;width:32px;height:32px;border:2px solid var(--white);border-radius:50%}
.fcol h3{font:500 18px 'Roboto',sans-serif;margin-bottom:20px}
.quick{left:349px;top:2098px}
.quick li{list-style:none;font:500 12.5px/26px 'Raleway',sans-serif}
.contact{left:543px;top:2098px}
.crow{display:flex;gap:12px;font:500 14px/21px 'Raleway',sans-serif;margin-bottom:16px}
.crow small{font-size:12.5px}
.form{left:831px;top:2098px}
.form .row{display:flex;gap:6px}
.field{border:1px solid var(--white);border-radius:4px;height:36px;font:400 11px 'Raleway',sans-serif;padding:10px 12px}
.field.half{width:131px}
.field.msg{width:268px;height:66px;margin-top:6px}
.send{margin-top:16px;width:120px;height:38px;background:var(--green);border-radius:2px;font:600 12px 'Raleway',sans-serif;display:flex;align-items:center;justify-content:center}
.bottom{left:0;top:2346px;width:1200px;height:70px;background:linear-gradient(var(--green),var(--green-dark));color:var(--white);font:400 14px 'Raleway',sans-serif;padding:34px 0 0 97px}
</style>
</head>
<body>

<div class="abs topline"></div>
<div class="abs topbar">
  <span><svg width="16" height="12" viewBox="0 0 16 12"><rect x="1" y="1" width="14" height="10" rx="1" fill="none" stroke="#fff" stroke-width="1.6"/><path d="M1 1l7 6 7-6" fill="none" stroke="#fff" stroke-width="1.6"/></svg>info@guardlinesecurity.com</span>
  <span><svg width="14" height="14" viewBox="0 0 24 24"><path fill="#fff" d="M6.6 10.8a15 15 0 006.6 6.6l2.2-2.2c.3-.3.7-.4 1-.2 1.1.4 2.3.6 3.6.6.6 0 1 .4 1 1V20c0 .6-.4 1-1 1A17 17 0 013 4c0-.6.4-1 1-1h3.5c.6 0 1 .4 1 1 0 1.3.2 2.5.6 3.6.1.3 0 .7-.2 1z"/></svg>+1 800 555 0199</span>
</div>

<div class="abs brand"><i></i>Guardline Security</div>
<nav class="abs mainnav"><span>Private Investigations</span><span>Surveillance Audit</span><span>Compliance Investigations</span><span>Contact Us</span></nav>

<div class="abs navbar">
  <ul>
    <li class="active">Home</li><li>About Us</li><li>Our Staff</li><li>MMJ Trasnport &amp; Courier Services</li><li>Our Vehicles</li><li>Alarm Systems</li><li>Video Systems</li>
  </ul>
</div>

<header class="abs hero" role="img" aria-label="Night-time banner with a wall-mounted security camera">
  <h1>Blog Posts</h1>
</header>

<div class="abs blog-title"><em>GUARDLINE SECURITY</em> BLOG</div>
<div class="abs blog-sub"><b></b>ENFORCEMENT SOLUTIONS<b></b></div>

<article class="abs post" style="top:575px">
  <div class="photo" role="img" aria-label="Security camera in a blurred lounge interior" style="background:linear-gradient(120deg,#d9cbbf,#c76a5c 40%,#efe6dc 75%,#b7a595)"></div>
  <h2>SECURITY &amp; SURVEILLANCE</h2>
  <div class="meta">
    <span><svg width="12" height="13" viewBox="0 0 12 13"><circle cx="6" cy="3.5" r="3" fill="currentColor"/><path d="M0 13c0-4 2.5-6 6-6s6 2 6 6z" fill="currentColor"/></svg>Posted by admin</span>
    <span><svg width="13" height="13" viewBox="0 0 13 13"><rect x=".8" y="2" width="11.4" height="10.2" fill="none" stroke="currentColor" stroke-width="1.4"/><path d="M.8 5h11.4" stroke="currentColor" stroke-width="1.4"/></svg>on June 21, 2016</span>
    <span><svg width="14" height="12" viewBox="0 0 14 12"><path d="M7 1C3.5 1 1 3 1 5.3c0 1.3.8 2.4 2 3.1L2.5 11 5.6 9.4c.5.1.9.1 1.4.1 3.5 0 6-2 6-4.2S10.5 1 7 1z" fill="none" stroke="currentColor" stroke-width="1.4"/></svg>Comments: 0</span>
  </div>
  <p class="p1">Lorem ipsum dolor sit amet, consectetur adipiscing elit, sed do eiusmod tempor incididunt ut labore et dolore magna aliqua. Ut enim ad minim veniam, quis nostrud exercitation ullamco laboris nisi ut aliquip ex ea commodo consequat. Duis aute irure dolor in reprehenderit in voluptate velit esse cillum dolore eu fugiat nulla pariatur. Excepteur sint occaecat cupidatat non proident, sunt in culpa qui</p>
  <p class="p2">Sed ut perspiciatis unde omnis iste natus error sit voluptatem accusantium doloremque laudantium, totam rem aperiam, eaque ipsa quae ab illo inventore veritatis et quasi architecto beatae vitae dicta sunt explicabo. Nemo enim ipsam voluptatem quia voluptas sit aspernatur aut odit aut fugit,</p>
  <div class="readmore">Read More</div>
</article>
<div class="abs divider" style="top:912px"></div>

<article class="abs post" style="top:948px">
  <div class="photo" role="img" aria-label="Operator watching camera feeds on several monitors" style="background:linear-gradient(100deg,#3b4a57,#7c8c99 45%,#d8dee4 70%,#eef1f4)"></div>
  <h2>TOTAL INTEGRATION</h2>
  <div class="meta">
    <span><svg width="12" height="13" viewBox="0 0 12 13"><circle cx="6" cy="3.5" r="3" fill="currentColor"/><path d="M0 13c0-4 2.5-6 6-6s6 2 6 6z" fill="currentColor"/></svg>Posted by admin</span>
    <span><svg width="13" height="13" viewBox="0 0 13 13"><rect x=".8" y="2" width="11.4" height="10.2" fill="none" stroke="currentColor" stroke-width="1.4"/><path d="M.8 5h11.4" stroke="currentColor" stroke-width="1.4"/></svg>on June 21, 2016</span>
    <span><svg width="14" height="12" viewBox="0 0 14 12"><path d="M7 1C3.5 1 1 3 1 5.3c0 1.3.8 2.4 2 3.1L2.5 11 5.6 9.4c.5.1.9.1 1.4.1 3.5 0 6-2 6-4.2S10.5 1 7 1z" fill="none" stroke="currentColor" stroke-width="1.4"/></svg>Comments: 0</span>
  </div>
  <p class="p1">Lorem ipsum dolor sit amet, consectetur adipiscing elit, sed do eiusmod tempor incididunt ut labore et dolore magna aliqua. Ut enim ad minim veniam, quis nostrud exercitation ullamco laboris nisi ut aliquip ex ea commodo consequat. Duis aute irure dolor in reprehenderit in voluptate velit esse cillum dolore eu fugiat nulla pariatur. Excepteur sint occaecat cupidatat non proident, sunt in culpa qui</p>
  <p class="p2">Sed ut perspiciatis unde omnis iste natus error sit voluptatem accusantium doloremque laudantium, totam rem aperiam, eaque ipsa quae ab illo inventore veritatis et quasi architecto beatae vitae dicta sunt explicabo. Nemo enim ipsam voluptatem quia voluptas sit aspernatur aut odit aut fugit,</p>
  <div class="readmore">Read More</div>
</article>
<div class="abs divider" style="top:1285px"></div>

<article class="abs post" style="top:1321px">
  <div class="photo" role="img" aria-label="Guard with a radio in a control room of video walls" style="background:linear-gradient(100deg,#2e3a44,#5d6d7a 45%,#aab8c4 70%,#dfe6ec)"></div>
  <h2>INFORMATION TECHNOLOGY</h2>
  <div class="meta">
    <span><svg width="12" height="13" viewBox="0 0 12 13"><circle cx="6" cy="3.5" r="3" fill="currentColor"/><path d="M0 13c0-4 2.5-6 6-6s6 2 6 6z" fill="currentColor"/></svg>Posted by admin</span>
    <span><svg width="13" height="13" viewBox="0 0 13 13"><rect x=".8" y="2" width="11.4" height="10.2" fill="none" stroke="currentColor" stroke-width="1.4"/><path d="M.8 5h11.4" stroke="currentColor" stroke-width="1.4"/></svg>on June 21, 2016</span>
    <span><svg width="14" height="12" viewBox="0 0 14 12"><path d="M7 1C3.5 1 1 3 1 5.3c0 1.3.8 2.4 2 3.1L2.5 11 5.6 9.4c.5.1.9.1 1.4.1 3.5 0 6-2 6-4.2S10.5 1 7 1z" fill="none" stroke="currentColor" stroke-width="1.4"/></svg>Comments: 0</span>
  </div>
  <p class="p1">Lorem ipsum dolor sit amet, consectetur adipiscing elit, sed do eiusmod tempor incididunt ut labore et dolore magna aliqua. Ut enim ad minim veniam, quis nostrud exercitation ullamco laboris nisi ut aliquip ex ea commodo consequat. Duis aute irure dolor in reprehenderit in voluptate velit esse cillum dolore eu fugiat nulla pariatur. Excepteur sint occaecat cupidatat non proident, sunt in culpa qui</p>
  <p class="p2">Sed ut perspiciatis unde omnis iste natus error sit voluptatem accusantium doloremque laudantium, totam rem aperiam, eaque ipsa quae ab illo inventore veritatis et quasi architecto beatae vitae dicta sunt explicabo. Nemo enim ipsam voluptatem quia voluptas sit aspernatur aut odit aut fugit,</p>
  <div class="readmore">Read More</div>
</article>
<div class="abs divider" style="top:1658px"></div>

<article class="abs post" style="top:1694px">
  <div class="photo" role="img" aria-label="Dome camera above a blurred warehouse aisle" style="background:linear-gradient(90deg,#9aa6ae,#d5dde2 50%,#8e9aa3)"></div>
  <h2>ACCESS CONTROL</h2>
  <div class="meta">
    <span><svg width="12" height="13" viewBox="0 0 12 13"><circle cx="6" cy="3.5" r="3" fill="currentColor"/><path d="M0 13c0-4 2.5-6 6-6s6 2 6 6z" fill="currentColor"/></svg>Posted by admin</span>
    <span><svg width="13" height="13" viewBox="0 0 13 13"><rect x=".8" y="2" width="11.4" height="10.2" fill="none" stroke="currentColor" stroke-width="1.4"/><path d="M.8 5h11.4" stroke="currentColor" stroke-width="1.4"/></svg>on June 21, 2016</span>
    <span><svg width="14" height="12" viewBox="0 0 14 12"><path d="M7 1C3.5 1 1 3 1 5.3c0 1.3.8 2.4 2 3.1L2.5 11 5.6 9.4c.5.1.9.1 1.4.1 3.5 0 6-2 6-4.2S10.5 1 7 1z" fill="none" stroke="currentColor" stroke-width="1.4"/></svg>Comments: 0</span>
  </div>
  <p class="p1">Lorem ipsum dolor sit amet, consectetur adipiscing elit, sed do eiusmod tempor incididunt ut labore et dolore magna aliqua. Ut enim ad minim veniam, quis nostrud exercitation ullamco laboris nisi ut aliquip ex ea commodo consequat. Duis aute irure dolor in reprehenderit in voluptate velit esse cillum dolore eu fugiat nulla pariatur. Excepteur sint occaecat cupidatat non proident, sunt in culpa qui</p>
  <p class="p2">Sed ut perspiciatis unde omnis iste natus error sit voluptatem accusantium doloremque laudantium, totam rem aperiam, eaque ipsa quae ab illo inventore veritatis et quasi architecto beatae vitae dicta sunt explicabo. Nemo enim ipsam voluptatem quia voluptas sit aspernatur aut odit aut fugit,</p>
  <div class="readmore">Read More</div>
</article>

<footer class="abs footer"></footer>
<div class="abs badge" role="img" aria-label="Partner badge"></div>
<div class="abs social" aria-label="Social links"><i></i><i></i><i></i><i></i></div>

<div class="abs fcol quick">
  <h3>QUICK LINK</h3>
  <ul><li>&gt;&nbsp; Home</li><li>&gt;&nbsp; About Us</li><li>&gt;&nbsp; Services</li><li>&gt;&nbsp; Blog</li><li>&gt;&nbsp; News</li><li>&gt;&nbsp; Contact Us</li></ul>
</div>

<div class="abs fcol contact">
  <h3>CONTACT US</h3>
  <div class="crow"><svg width="12" height="16" viewBox="0 0 12 16"><path d="M6 0a6 6 0 00-6 6c0 4.5 6 10 6 10s6-5.5 6-10a6 6 0 00-6-6z" fill="#8cc31e"/><circle cx="6" cy="6" r="2.3" fill="#1676a6"/></svg><div>Guardline Security,<br><small>4th Floor, 18 Harbour Lane,<br>Westford.</small></div></div>
  <div class="crow"><svg width="14" height="14" viewBox="0 0 24 24"><path fill="#8cc31e" d="M6.6 10.8a15 15 0 006.6 6.6l2.2-2.2c.3-.3.7-.4 1-.2 1.1.4 2.3.6 3.6.6.6 0 1 .4 1 1V20c0 .6-.4 1-1 1A17 17 0 013 4c0-.6.4-1 1-1h3.5c.6 0 1 .4 1 1 0 1.3.2 2.5.6 3.6.1.3 0 .7-.2 1z"/></svg><div>Help:&nbsp; +1 800 555 0199</div></div>
  <div class="crow"><svg width="14" height="11" viewBox="0 0 16 12"><rect x="0" y="0" width="16" height="12" rx="1" fill="#8cc31e"/><path d="M1 1l7 6 7-6" fill="none" stroke="#1676a6" stroke-width="1.4"/></svg><div>Mail:&nbsp; info@guardlinesecurity.com</div></div>
</div>

<div class="abs fcol form">
  <h3>CONTACT FORM</h3>
  <div class="row"><div class="field half">Name</div><div class="field half">Phone</div></div>
  <div class="field msg">Message</div>
  <div class="send">SEND MESSAGE</div>
</div>

<div class="abs bottom">© 2016 Guardline Security.All Rights Reserved.</div>

</body>
</html>
```